Redesign of Plastic Surgeon Website to fully responsive / modern feel

Hi

Our current website is out of date www.harbourlinecosmetic.org

We want a fresh / modern looking design
Needs to be fully responsive design that works extremely well on ipad and mobile device

Would like design for both full screen website and mobile

Have listed a few websites of other plastic surgeons we like
http://www.reformclinicdaily.com/
http://www.peterholtbymd.com/
http://www.corvanbeauty.com/
http://www.tidewellcontouring.com/

Menu needs to include
1. About Us
2. Procedures (see current website for example)
3. News
4. Patient Resources
5. Contact Us

We are flexible with colours / images / layout

I have uploaded a document that has some content - the face pages content is completed only

some of the procedures can have content upwards of 4000 words - total website can be large with over 40,000 words
Updates

Target Market(s)

Mainly women 20-60 85% of practice
Some men 15%

Industry/Entity Type

Plastic Surgery

Number of Pages Required

5+ page

Requirements
Must have
• We need designs for
• Homepage
• Internal pages
• 1. Landing pages for breast / body / face / non surgical main pages
• 2. Procedure pages for individual pages under each section - eg breast augmentation
• 3. About us pages - like meet the doctor, our staff, clinics
• 4. Contact page
• 5. Blog / News page
Nice to have
• See our list of websites for examples of designs we like
• Like full screen design with nice hero image
• Needs to have good to call to action messages on home page like
• Specials, procedure of the month, etc

```html
<!DOCTYPE html>
<html lang="en">
<head>
<meta charset="utf-8">
<title>Harbourline Cosmetic Institute</title>
<link rel="stylesheet" href="https://fonts.googleapis.com/css2?family=Open+Sans:wght@400;600&family=Poppins:wght@600&family=Raleway:wght@300;400;500&display=swap">
<style>
:root{
  --ink:#000;
  --white:#fff;
  --skin:#c3a596;
  --skin-light:#dcc4b8;
  --hair:#3a2b24;
  --hair-mid:#55443b;
  --hero-base:#75695f;
  --hero-low:#5c5957;
  --panel:#ebebeb;
  --muted:#6a6a6a;
  --line:rgba(255,255,255,.9);
}
*{box-sizing:border-box;margin:0;padding:0}
html,body{width:777px;height:1200px;overflow:hidden;background:var(--ink)}
body{position:relative;font-family:"Open Sans",sans-serif;color:var(--white)}

.hero{position:absolute;left:0;top:0;width:777px;height:615px;
  background:
    linear-gradient(180deg,rgba(0,0,0,0) 0%,rgba(0,0,0,0) 62%,rgba(80,78,77,.85) 78%,var(--hero-low) 100%),
    radial-gradient(ellipse 190px 230px at 470px 230px,var(--skin-light) 0%,var(--skin) 45%,rgba(195,165,150,0) 100%),
    radial-gradient(ellipse 170px 260px at 170px 260px,var(--hair) 0%,rgba(58,43,36,.6) 55%,rgba(58,43,36,0) 100%),
    radial-gradient(ellipse 160px 200px at 700px 170px,var(--hair-mid) 0%,rgba(85,68,59,0) 100%),
    radial-gradient(ellipse 260px 120px at 390px 60px,#4b3c34 0%,rgba(75,60,52,0) 100%),
    var(--hero-base)}
.hero::after{content:"";position:absolute;inset:0;background:rgba(40,36,34,.28)}

.site-header{position:absolute;left:0;top:0;width:777px;height:53px;background:rgba(25,23,22,.55);border-bottom:1px solid rgba(255,255,255,.35)}
.brand{position:absolute;left:40px;top:0;width:94px;height:110px;background:#050505;border-radius:0 0 10px 10px;box-shadow:0 2px 6px rgba(0,0,0,.4);display:flex;flex-direction:column;justify-content:center;align-items:center;text-align:center;font-family:"Raleway",sans-serif;font-weight:500;font-size:10.5px;line-height:14px;letter-spacing:.8px;text-transform:uppercase;color:var(--white);z-index:2}
.main-nav a{position:absolute;top:26px;font-size:7.5px;color:var(--white);text-decoration:none;text-transform:uppercase}

.headline{position:absolute;left:0;top:206px;width:777px;text-align:center;font-family:"Poppins",sans-serif;font-weight:600;font-size:27.5px;line-height:34px;text-transform:uppercase;letter-spacing:.6px;text-shadow:0 1px 3px rgba(0,0,0,.25)}

.connector{position:absolute;left:157px;top:441px;width:441px;height:1.5px;background:var(--line)}
.area-icon{position:absolute;top:397px;width:88px;height:88px;border-radius:50%;border:2px solid var(--white);box-shadow:0 0 0 2px rgba(0,0,0,.35)}
.area-icon.light{background:var(--white)}
.area-icon.dark{background:#050505}
.area-icon::after{content:"";position:absolute;left:25px;top:14px;width:34px;height:56px;border-radius:17px}
.area-icon.light::after{background:linear-gradient(#2a2a2a,#8a8a8a);left:22px;top:18px;width:40px;height:48px;border-radius:20px 20px 14px 14px}
.area-icon.dark::after{background:linear-gradient(#f2f2f2,#bdbdbd)}
.area-icon.breast::after{left:22px;top:20px;width:40px;height:46px;border-radius:10px;background:none;border:1.5px dashed #eee}

.area-card{position:absolute;top:490px;width:170px;text-align:center}
.area-card h3{font-size:11px;font-weight:600;margin-bottom:9px}
.area-card p{font-size:7.2px;line-height:10.4px;color:#eee}
.area-card .more{display:inline-block;margin-top:7px;font-size:7.5px;color:var(--white)}
.area-card .more::after{content:"";display:inline-block;margin-left:5px;border-left:3px solid var(--white);border-top:3px solid transparent;border-bottom:3px solid transparent}

.about{position:absolute;left:0;top:615px;width:777px;height:228px;background:var(--ink);text-align:center}
.about h2{font-family:"Raleway",sans-serif;font-weight:300;font-size:19px;margin-top:30px}
.about p{width:620px;margin:15px auto 0;font-size:8.4px;line-height:14.8px}
.about p+p{margin-top:14px}
.btn{display:block;width:87px;height:23px;margin:14px auto 0;background:var(--white);color:#222;font-size:7px;line-height:23px;text-decoration:none}

.testimonials{position:absolute;left:0;top:843px;width:777px;height:275px;
  background:
    radial-gradient(ellipse 160px 120px at 560px 250px,rgba(245,242,240,.9) 0%,rgba(245,242,240,0) 100%),
    linear-gradient(90deg,#a88a7c 0%,#cdb3a6 30%,#dcc6ba 55%,#cdb2a4 75%,#a38678 100%)}
.testimonials h2{position:absolute;left:0;top:28px;width:777px;text-align:center;font-family:"Raleway",sans-serif;font-weight:400;font-size:22px}
.quote-mark{position:absolute;font-family:Georgia,serif;font-style:italic;font-weight:700;font-size:30px;color:#222}
.quote-card{position:absolute;left:80px;top:94px;width:596px;height:97px;background:var(--panel);border-radius:3px}
.avatar{position:absolute;left:24px;top:16px;width:70px;height:70px;border-radius:50%;border:2px solid var(--white);background:linear-gradient(#e8e8e8 0%,#c9b09d 45%,#2e3138 70%,#23262c 100%)}
.quote-card p{position:absolute;left:112px;top:26px;width:455px;font-size:9.2px;line-height:13.2px;color:var(--muted)}
.quote-card cite{position:absolute;right:40px;top:74px;font-style:normal;font-weight:600;font-size:10px;color:#222}
.dots{position:absolute;left:371px;top:229px;display:flex;gap:4px}
.dots span{width:8px;height:8px;border-radius:50%;border:1px solid var(--white)}
.dots span.on{background:var(--white)}

.site-footer{position:absolute;left:0;top:1118px;width:777px;height:82px;background:#050505;text-align:center}
.footer-links{margin-top:29px;font-size:7.5px}
.footer-links a{color:var(--white);text-decoration:none}
.copyright{margin-top:6px;font-size:6px}
.social{position:absolute;right:46px;top:40px;display:flex;gap:17px}
.social span{width:7px;height:7px;border-radius:50%;background:#bbb}
</style>
</head>
<body>
<div class="hero" role="img" aria-label="Close-up portrait photograph of a woman with curled brown hair"></div>

<header class="site-header">
  <div class="brand">Harbour<br>line<br>Cosmetic<br>Institute</div>
  <nav class="main-nav">
    <a href="#" style="left:339px">Home</a>
    <a href="#" style="left:394px">About Us</a>
    <a href="#" style="left:464px">Procedures</a>
    <a href="#" style="left:542px">News</a>
    <a href="#" style="left:596px">Patient Resources</a>
    <a href="#" style="left:700px">Contact Us</a>
  </nav>
</header>

<h1 class="headline">Invest in yourself, renew your<br>look and refresh your confidence</h1>

<div class="connector"></div>
<div class="area-icon light" style="left:113px" role="img" aria-label="Face procedures icon"></div>
<div class="area-icon dark" style="left:333px" role="img" aria-label="Body procedures icon"></div>
<div class="area-icon dark breast" style="left:554px" role="img" aria-label="Breast procedures icon"></div>

<div class="area-card" style="left:78px">
  <h3>Face</h3>
  <p>Lorem ipsum dolor sit amet, consectetur edit adipiscing elit, sed do eiusmod tempor incididunt utdolore magna aliqua.</p>
  <a class="more">Read More</a>
</div>
<div class="area-card" style="left:297px;top:492px">
  <h3>Body</h3>
  <p>Lorem ipsum dolor sit amet, consectetur edit adipiscing elit, sed do eiusmod tempor incididunt utdolore magna aliqua.</p>
  <a class="more" style="margin-top:4px">Read More</a>
</div>
<div class="area-card" style="left:518px">
  <h3>Breast</h3>
  <p>Lorem ipsum dolor sit amet, consectetur edit adipiscing elit, sed do eiusmod tempor incididunt utdolore a aliqua.</p>
  <a class="more" style="margin-top:4px">Read More</a>
</div>

<section class="about">
  <h2>Harbourline Cosmetic Institute</h2>
  <p>You can expect beautiful results at the Harbourline Cosmetic Institute. With expertise in facelifts, breast augmentation or breast reduction and liposuction body contouring, we offer total care at every step of your transformative journey.</p>
  <p>Dr Whitcombe is one of Australia’s most eminent specialists in plastic surgery, reconstructive and aesthetic surgery, and is supported by our highly qualified, professional team. As the premier plastic surgery clinic in Harbourline, we use only the most revolutionary techniques to minimise scarring, we help you look better, feel better and enjoy a beautiful new you.</p>
  <a class="btn" href="#">READMORE</a>
</section>

<section class="testimonials" role="region" aria-label="Testimonials over a soft skin-toned photograph">
  <h2>Our Testimonials</h2>
  <span class="quote-mark" style="left:83px;top:62px">“</span>
  <div class="quote-card">
    <div class="avatar" role="img" aria-label="Portrait photo of a smiling man in a suit"></div>
    <p>Lorem ipsum dolor sit amet, consectetur adipiscing elit, sed do eiusmod tempor incididunt ut labore et dolore magna aliqua. Ut enim ad minim veniam, quis nostrud exercitation ullamco laboris nisi ut aliquip ex ea commodo consequat.</p>
    <cite>- Daniel Hartley</cite>
  </div>
  <span class="quote-mark" style="left:657px;top:200px">”</span>
  <div class="dots"><span></span><span class="on"></span><span></span></div>
</section>

<footer class="site-footer">
  <div class="footer-links"><a href="#">Home</a> / <a href="#">About us</a> / <a href="#">Service Us</a> / <a href="#">Contact Us</a></div>
  <div class="copyright">© All Rights Reserved. Copyrights @CompanyName .2016</div>
  <div class="social"><span></span><span></span><span></span><span></span><span></span></div>
</footer>
</body>
</html>
```